Business Card

I need a business card that really pops for a potential customer or person who refers a personal injury lead. I want to highlight our office locations, but only address that needs to be on the card is my office's main address. I want a sleek, modern and minimalist design.

```html
<!DOCTYPE html>
<html lang="en">
<head>
<meta charset="utf-8">
<title>Northgate Injury Counsel – Business Card</title>
<link href="https://fonts.googleapis.com/css2?family=Jost:wght@400;500;600&display=swap" rel="stylesheet">
<style>
  :root {
    --bg: #262626;
    --card-front: #2f2f2f;
    --card-back: #363636;
    --front-ink: #767676;
    --ink: #f2f2f2;
    --ink-soft: #d9d9d9;
    --rule: #8a8a8a;
  }
  * { margin: 0; padding: 0; box-sizing: border-box; }
  html, body { width: 1200px; height: 689px; overflow: hidden; }
  body {
    background: var(--bg);
    font-family: "Jost", sans-serif;
    color: var(--ink);
  }
  .stage {
    position: relative;
    width: 1200px;
    height: 689px;
    display: flex;
    align-items: center;
    justify-content: center;
    gap: 60px;
  }
  .card {
    position: relative;
    width: 520px;
    height: 297px;
    border-radius: 18px;
    box-shadow: 0 14px 30px rgba(0,0,0,0.45);
  }
  .card--front { background: var(--card-front); }
  .card--back { background: var(--card-back); }

  .firm-name {
    position: absolute;
    font-weight: 500;
    white-space: nowrap;
    line-height: 1;
  }
  .card--front .firm-name {
    left: 50%;
    top: 50%;
    transform: translate(-50%, -50%);
    font-size: 30px;
    color: var(--front-ink);
  }
  .card--back .firm-name {
    left: 30px;
    top: 50%;
    transform: translateY(-50%);
    font-size: 18px;
    color: var(--ink);
  }

  .divider {
    position: absolute;
    left: 262px;
    top: 34px;
    width: 1px;
    height: 200px;
    background: linear-gradient(to bottom, transparent, var(--rule) 20%, var(--rule) 80%, transparent);
  }
  .contact {
    position: absolute;
    left: 282px;
    top: 40px;
    font-size: 12px;
    line-height: 1.35;
    color: var(--ink-soft);
  }
  .contact__name { font-weight: 600; font-size: 18px; color: var(--ink); letter-spacing: 0.3px; }
  .contact__role { font-size: 11.5px; margin-bottom: 14px; }
  .contact__address { margin-bottom: 14px; }
  .contact__list { list-style: none; }
  .contact__item { display: flex; align-items: center; gap: 8px; }
  .contact__item svg { width: 10px; height: 10px; fill: var(--ink); flex: none; }
</style>
</head>
<body>
<main class="stage">
  <section class="card card--front" aria-label="Card front">
    <div class="firm-name">Northgate Injury Counsel</div>
  </section>

  <section class="card card--back" aria-label="Card back">
    <div class="firm-name">Northgate Injury Counsel</div>
    <div class="divider"></div>
    <div class="contact">
      <div class="contact__name">DANIEL REYES</div>
      <div class="contact__role">President</div>
      <div class="contact__address">240 West Harbor Street<br>Suite 1810<br>Lakeport, IL 60690</div>
      <ul class="contact__list">
        <li class="contact__item">
          <svg viewBox="0 0 10 10"><path d="M2 0.5 L3.8 2.6 L2.9 3.8 Q4 6 6.2 7.1 L7.4 6.2 L9.5 8 L8.3 9.5 Q4.5 9.3 2.3 7.4 Q0.6 5.4 0.5 1.7 Z"/></svg>
          312-555-0148
        </li>
        <li class="contact__item">
          <svg viewBox="0 0 10 10"><path d="M2.5 0 H7.5 V10 H2.5 Z M3.3 1 V8 H6.7 V1 Z" fill-rule="evenodd"/></svg>
          312-555-0192
        </li>
        <li class="contact__item">
          <svg viewBox="0 0 10 10"><path d="M0 2 H10 V8.5 H0 Z M0.8 2.6 L5 5.8 L9.2 2.6 Z" fill-rule="evenodd"/></svg>
          info@northgateinjurycounsel.com
        </li>
        <li class="contact__item">
          <svg viewBox="0 0 10 10"><circle cx="5" cy="5" r="4.6"/></svg>
          northgateinjurycounsel.com
        </li>
      </ul>
    </div>
  </section>
</main>
</body>
</html>
```